依頼詳細
サイズが決まっています。添付データのサイズを参照してください。
モルテナカタログのような感じのデザインをお願いします。
記載項目
日常生活に支援が必要な方、支援をする方へ『あんしん』をお届けします。

使いやすい、見やすい、分かりやすい
希望イメージ
シンプル 複雑
単色 カラフル
暗い 明るい
日常 高級
遊び心 厳粛
未来的 伝統的
女性的 男性的
希望する色
青系、緑系
納品ファイル
• イラストレーター形式 (.ai)
補足説明
”カタログの表紙を別刷り”というのは
添付したSOFT ROAD の下のオレンジの枠内を差し替えるということです。
依頼内容が分かりにくいようで失礼いたしました。
■ 選んだ理由

今回、当カタログの取り扱い品目と安心を届けるというコンセプトに合致している点、そして社内での投票をさせて頂きました結果、korumi様のご提案を採用させて戴きました。

■ 提案者全員のお礼・コメント

今度は本当に沢山のご提案をいただきまして有難うございました。
どのランサーの方の提案も素晴らしいものばかりでしたが、
上記理由により、社内で最も票の多かった提案を採用させて頂きました。

```html
<!DOCTYPE html>
<html lang="ja">
<head>
<meta charset="utf-8">
<title>SOFT ROAD 福祉用具総合カタログ</title>
<link rel="stylesheet" href="https://fonts.googleapis.com/css2?family=Oswald:wght@600&family=Noto+Sans+JP:wght@500;700&family=Noto+Serif+JP:wght@700&display=swap">
<style>
  :root{
    --paper:#ffffff;
    --green:#3f9a48;
    --coral:#e8475b;
    --ink:#333a44;
    --navy:#1d4f93;
    --blue:#2769b4;
    --sky:#4b92d3;
    --tile:#3a80c6;
    --white:#ffffff;
  }
  *{margin:0;padding:0;box-sizing:border-box}
  html,body{width:849px;height:1200px;overflow:hidden;background:var(--paper)}
  .cover{position:relative;width:849px;height:1200px;background:var(--paper);font-family:"Noto Sans JP",sans-serif;color:var(--ink)}
  .kicker{position:absolute;top:30px;width:100%;text-align:center;color:var(--green);font-weight:700;font-size:30px;letter-spacing:3px}
  .title{position:absolute;top:72px;width:100%;text-align:center;font-family:"Oswald",sans-serif;font-weight:600;font-size:168px;line-height:1;color:var(--coral);letter-spacing:10px}
  .tagline{position:absolute;top:262px;width:100%;text-align:center;font-family:"Oswald",sans-serif;font-size:20px;letter-spacing:4px;color:var(--ink)}
  .panel{position:absolute;left:34px;top:300px;width:781px;height:818px;background:linear-gradient(160deg,var(--blue),var(--navy))}
  .tile{position:absolute;background:var(--tile)}
  .art{position:absolute;border-radius:4px}
  .label{position:absolute;font-size:13px;color:var(--white);font-weight:500}
  .intro{position:absolute;left:48px;top:22px;width:258px;padding:10px 12px;border:2px solid var(--white);color:var(--white);font-size:17px;line-height:1.55;font-weight:700;background:var(--navy)}
  .lead{position:absolute;top:446px;width:100%;text-align:center;color:var(--white);font-weight:700;font-size:24px;letter-spacing:2px}
  .headline{position:absolute;top:488px;width:100%;text-align:center;color:var(--white);font-family:"Noto Serif JP",serif;font-weight:700;font-size:64px;letter-spacing:4px}
  .sub{position:absolute;top:572px;width:100%;text-align:center;color:var(--white);font-size:18px;letter-spacing:1px}
  .maker{position:absolute;top:1138px;width:100%;display:flex;justify-content:center;align-items:center;gap:14px;font-weight:700;font-size:30px;color:var(--ink);letter-spacing:2px}
  .maker .mark{width:30px;height:30px;background:var(--ink)}
</style>
</head>
<body>
<main class="cover">
  <p class="kicker">福祉用具総合カタログ</p>
  <h1 class="title">SOFT ROAD</h1>
  <p class="tagline">FOR GOOD HAPPINESS HUMAN LIFE</p>

  <section class="panel">
    <div class="tile" style="left:0;top:0;width:492px;height:440px;background:var(--sky)"></div>
    <div class="art" role="img" aria-label="介護用ベッドとクッションのイラスト" style="left:40px;top:120px;width:420px;height:300px;background:linear-gradient(180deg,#b9d4ee,#7fb0de)"></div>
    <span class="label" style="left:20px;top:412px">特殊寝台＆付属品</span>
    <p class="intro">日常生活に支援が必要な方、支援をする方へ「あんしん」をお届けします。</p>

    <div class="tile" style="left:500px;top:0;width:281px;height:262px"></div>
    <div class="art" role="img" aria-label="車いすのイラスト" style="left:560px;top:20px;width:190px;height:210px;background:linear-gradient(180deg,#d8a4a8,#8fa6bf)"></div>
    <span class="label" style="left:708px;top:238px">車いす</span>

    <div class="tile" style="left:500px;top:270px;width:281px;height:170px;background:var(--sky)"></div>
    <div class="art" role="img" aria-label="歩行補助つえのイラスト" style="left:600px;top:282px;width:100px;height:140px;background:linear-gradient(180deg,#d2dde8,#9bb0c4)"></div>
    <span class="label" style="left:680px;top:414px">歩行補助つえ</span>

    <p class="lead">＼ 使いやすい、見やすい、分かりやすい ／</p>
    <p class="headline">介護に「あんしん」を</p>
    <p class="sub">nursing care assisting article.</p>

    <div class="tile" style="left:22px;top:610px;width:226px;height:208px"></div>
    <div class="art" role="img" aria-label="歩行器のイラスト" style="left:60px;top:628px;width:150px;height:160px;background:linear-gradient(180deg,#e4ebf2,#a9bdd0)"></div>
    <span class="label" style="left:30px;top:792px">歩行器</span>

    <div class="tile" style="left:270px;top:610px;width:240px;height:208px;background:var(--sky)"></div>
    <div class="art" role="img" aria-label="手すりのイラスト" style="left:320px;top:628px;width:140px;height:160px;background:linear-gradient(180deg,#efe3cf,#b9a27e)"></div>
    <span class="label" style="left:430px;top:792px">手すり</span>

    <div class="tile" style="left:532px;top:610px;width:249px;height:208px"></div>
    <div class="art" role="img" aria-label="階段昇降リフトのイラスト" style="left:560px;top:624px;width:200px;height:170px;background:linear-gradient(160deg,#eef3f8,#a8bfd6)"></div>
    <span class="label" style="left:672px;top:796px">階段昇降リフト</span>
  </section>

  <footer class="maker"><span class="mark"></span><span>青葉ケア商事株式会社</span></footer>
</main>
</body>
</html>
```